Business Profile Landing Page for search engine Start UP " Amber Quill"

Hi there
Amber Quill is an search engine for the Amber Quill - business.

What i´m looking for is a stunning singel Profile Landing Page for the Companys presentation.

Following Details should be included.

1st section
Comapanys name
Adress
info row ( opening time or what ever)
Profile Picture Big ( Could be the logo)
+3 smaller Pictures ( Maybe the store, main product ...)

2nd Section
navigation Icons for:
Call, Mail , Web, Route, Data

3er Section
About us.

Text lines.....
+Pictures slider

4th Section
1 row : Products ( Titel , Picture, Price)
2nd row :Service ( same as Products + text lines )

5th section
Blog Posts row

.....................................................
Well thats all, Colors used from the logo, u can also use the favicon somewhere (the crown magnifying glass)

Target Market(s)

All Comapnys, it should be an " used for all" design

Number of Pages Required

1 page

Requirements
Must have
• The first sighting is the important part, so the " first section should be impressively and makes the customers curious about more informations (very important for mobile version)
Nice to have
• If you can insert our favicon somewhere would be cool, but its not nessesery
Should not have
• you dont need to make a header or footer, that part is already done. i just need the main section design

```html
<!DOCTYPE html>
<html lang="en">
<head>
<meta charset="UTF-8">
<title>Amber Quill – Business Profile</title>
<link rel="stylesheet" href="https://fonts.googleapis.com/css2?family=Poppins:wght@400;500;600;700&family=Open+Sans:wght@400;600;700&display=swap">
<style>
:root{
  --amber:#E4A000;
  --amber-deep:#C98A00;
  --ink:#2B2B2B;
  --text:#4A4A4A;
  --muted:#8A8A8A;
  --cream:#F9F5EF;
  --grey:#EFEFEF;
  --white:#FFFFFF;
  --brown:#4B3535;
  --line:#E8C57A;
}
*{margin:0;padding:0;box-sizing:border-box}
html,body{width:1200px;height:3524px;overflow:hidden}
body{position:relative;background:var(--white);font-family:"Open Sans",Arial,sans-serif;color:var(--text)}
.abs{position:absolute}

/* Hero */
.hero-side{left:0;top:0;width:520px;height:583px;background:linear-gradient(135deg,#F3EEE7 0%,#EDE4D8 45%,#F6F1EA 100%)}
.hero-photo{left:520px;top:0;width:680px;height:583px;background:linear-gradient(160deg,#EDE8E4 0%,#C9B6A4 35%,#7A5A42 70%,#4E3626 100%)}
.brand-name{font-family:"Poppins",sans-serif;font-weight:700;color:var(--amber);font-size:46px;line-height:1;white-space:nowrap}
.hero-brand{left:107px;top:130px}
.hero-intro{left:107px;top:226px;width:330px;font-size:13px;line-height:27px;color:var(--text)}
.info-list{left:112px;top:382px;list-style:none}
.info-list li{display:flex;align-items:center;height:38px;font-size:14.5px;color:var(--ink)}
.info-list svg{width:22px;height:22px;margin-right:24px;flex:none}

/* Chevron badge */
.badge{left:520px;top:583px;width:159px;height:85px;z-index:2}

/* Feature tiles */
.band-cream{left:0;top:583px;width:1200px;height:290px;background:var(--cream)}
.tile{top:673px;width:333px;height:164px;border-radius:6px;display:flex;align-items:center;justify-content:center;color:var(--white);font-size:26px;font-weight:400;box-shadow:0 2px 6px rgba(0,0,0,.2)}
.tile-store{left:83px;background:linear-gradient(180deg,#6C6A66,#3E3B37)}
.tile-product{left:434px;background:linear-gradient(180deg,#8A8680,#5B5752)}
.tile-publicity{left:782px;background:linear-gradient(180deg,#7E8A86,#565B55)}

/* Contact navigation */
.band-grey{left:0;top:873px;width:1200px;height:293px;background:var(--grey)}
.nav-card{top:962px;width:157px;height:150px;background:var(--white);border-radius:8px;box-shadow:0 2px 6px rgba(0,0,0,.08)}
.nav-ring{top:919px;width:126px;height:126px;border-radius:50%;border:2px solid var(--amber);background:var(--white);display:flex;align-items:center;justify-content:center}
.nav-ring svg{width:60px;height:60px}
.nav-btn{top:1066px;width:149px;height:40px;background:var(--amber);border-radius:3px;display:flex;align-items:center;justify-content:center;font-family:"Poppins",sans-serif;font-weight:600;font-size:16px;color:var(--ink)}

/* About */
.section-title{left:0;width:1200px;text-align:center;font-family:"Poppins",sans-serif;font-weight:700;font-size:32px;color:var(--ink)}
.about-brand{left:0;width:1200px;top:1280px;text-align:center}
.about-brand .brand-name{font-size:52px}
.about-visual{left:211px;top:1572px;width:364px;height:364px;border-radius:50%;background:radial-gradient(circle at 50% 40%,#E9E6EE 0%,#9AA3B5 40%,#2F4968 75%,#1F3450 100%)}
.about-block{left:609px;width:420px}
.about-block h3{font-family:"Poppins",sans-serif;font-weight:600;font-size:20px;color:var(--amber-deep);padding-bottom:6px;border-bottom:1.5px solid var(--line)}
.about-block p{margin:12px 0 0 64px;font-size:13px;line-height:26.7px;color:var(--text)}

/* Gallery */
.gallery{top:2036px;height:251px}
.g1{left:0;width:320px;background:linear-gradient(180deg,#D9D6D2,#8C877F 70%,#3B3835)}
.g2{left:346px;width:506px;background:linear-gradient(135deg,#B88A5A 0%,#8C6440 40%,#2E2D30 75%,#1F1F22 100%)}
.g3{left:877px;width:323px;background:linear-gradient(180deg,#E2E8EC 0%,#A9B59A 45%,#8E8C86 75%,#6D6A66 100%)}

/* Offers */
.offer{left:171px;width:852px;height:208px;background:var(--white);box-shadow:0 2px 10px rgba(0,0,0,.08);display:flex}
.offer-info{width:245px;display:flex;flex-direction:column;align-items:center;justify-content:center;padding:0 24px}
.offer-info h4{font-family:"Poppins",sans-serif;font-weight:600;font-size:26px;line-height:26px;color:var(--amber);text-align:center;width:100%;padding-bottom:20px;border-bottom:1px solid #EAEAEA}
.offer-info p{font-size:13px;line-height:16px;color:var(--text);text-align:center;padding:14px 0;border-bottom:1px solid #EAEAEA;width:100%}
.offer-photo{width:366px;height:208px}
.photo-product{background:linear-gradient(120deg,#F2F2F2 0%,#DCDCDC 45%,#B9AFA6 70%,#E8E8E8 100%)}
.photo-service{background:linear-gradient(135deg,#8A6A5E 0%,#6E5048 40%,#3E5A7A 70%,#6A5046 100%)}
.offer-price{width:241px;display:flex;flex-direction:column;align-items:center;justify-content:center;padding:0 20px}
.offer-price strong{font-family:"Poppins",sans-serif;font-weight:700;font-size:44px;color:var(--ink);width:100%;text-align:center;padding-bottom:14px;border-bottom:1px solid #EAEAEA}
.offer-price span{font-family:"Poppins",sans-serif;font-size:14px;color:var(--ink);width:100%;text-align:center;padding:14px 0;border-bottom:1px solid #EAEAEA}

/* Blog */
.band-blog{left:0;top:2925px;width:1200px;height:465px;background:var(--cream)}
.post{top:3007px;width:245px;height:334px;background:var(--white);border-radius:6px;box-shadow:0 2px 8px rgba(0,0,0,.08);overflow:hidden}
.post-photo{height:157px}
.p1{background:linear-gradient(135deg,#7A2A22,#4A1A18 60%,#2B1414)}
.p2{background:linear-gradient(135deg,#B8C4D8,#8FA0BC 60%,#2A2E3A)}
.p3{background:linear-gradient(180deg,#F0EEE8,#C8BFB0 50%,#7A3A2A)}
.p4{background:linear-gradient(180deg,#E8E6E0,#B8B2A6 55%,#6A6258)}
.post-body{padding:14px 22px 0 22px}
.post-tag{font-size:11px;color:var(--amber)}
.post-title{font-weight:700;font-size:15px;line-height:16.5px;color:var(--ink);margin-top:8px;height:66px}
.post-text{font-size:11px;line-height:16px;color:var(--muted);margin-top:12px}

/* Newsletter */
.newsletter{left:0;top:3390px;width:1200px;height:134px;background:var(--brown)}
.news-title{left:151px;top:3440px;font-family:"Poppins",sans-serif;font-weight:600;font-size:26px;color:var(--white)}
.news-input{left:501px;top:3441px;width:418px;height:31px;border-radius:16px;background:#BDBDBD;font-size:11px;color:#5A5A5A;padding-left:58px;display:flex;align-items:center}
.news-btn{left:937px;top:3441px;width:111px;height:31px;border-radius:16px;background:var(--amber);font-family:"Poppins",sans-serif;font-weight:700;font-size:11px;color:var(--ink);display:flex;align-items:center;justify-content:center}
</style>
</head>
<body>

<!-- Hero -->
<div class="abs hero-side" role="img" aria-label="Soft, faded photo of a person in a knit sweater typing"></div>
<div class="abs hero-photo" role="img" aria-label="Hands typing on a laptop on a wooden table"></div>

<div class="abs hero-brand"><div class="brand-name">Amber Quill</div></div>

<p class="abs hero-intro">Vienna, Austria’s capital, lies in the country’s east on the Danube River. Its artistic and intellectual legacy was shaped by residents including Albrecht Venn, Jonas Keller and Emil Rauth.</p>

<ul class="abs info-list">
  <li><svg viewBox="0 0 24 24"><path d="M12 2a7 7 0 0 0-7 7c0 5 7 13 7 13s7-8 7-13a7 7 0 0 0-7-7z" fill="#E4A000"/><circle cx="12" cy="9" r="2.6" fill="#fff"/></svg>Lindenweg 42, Eastvale 4821 · Map</li>
  <li><svg viewBox="0 0 24 24"><circle cx="12" cy="12" r="9" fill="none" stroke="#E4A000" stroke-width="2"/><path d="M12 7v5l3 2" fill="none" stroke="#E4A000" stroke-width="2" stroke-linecap="round"/></svg>10 am - 09 pm</li>
  <li><svg viewBox="0 0 24 24"><path d="M6.6 10.8a15 15 0 0 0 6.6 6.6l2.2-2.2a1 1 0 0 1 1-.25 11.4 11.4 0 0 0 3.6.6 1 1 0 0 1 1 1V20a1 1 0 0 1-1 1A17 17 0 0 1 3 4a1 1 0 0 1 1-1h3.5a1 1 0 0 1 1 1c0 1.25.2 2.45.6 3.6a1 1 0 0 1-.25 1z" fill="#E4A000"/></svg>+43 1234 56789</li>
</ul>

<!-- Tiles -->
<div class="abs band-cream"></div>
<svg class="abs badge" viewBox="0 0 159 85"><path d="M0 0H159V60L79.5 85L0 60Z" fill="#E4A000"/><circle cx="79.5" cy="36" r="12" fill="none" stroke="#2B2B2B" stroke-width="3.5"/></svg>
<div class="abs tile tile-store" role="img" aria-label="Store front photo">Store</div>
<div class="abs tile tile-product" role="img" aria-label="Product photo">Product</div>
<div class="abs tile tile-publicity" role="img" aria-label="City street photo">Publicity</div>

<!-- Contact navigation -->
<div class="abs band-grey"></div>

<div class="abs nav-card" style="left:171px"></div>
<div class="abs nav-ring" style="left:187px"><svg viewBox="0 0 60 60" fill="none" stroke="#E4A000" stroke-width="2" stroke-linejoin="round"><path d="M10 22c0-6 8-9 20-9s20 3 20 9v3h-9v-5H19v5h-9z"/><path d="M18 27h24l4 20H14z"/><circle cx="30" cy="37" r="6"/></svg></div>
<div class="abs nav-btn" style="left:175px">Call</div>

<div class="abs nav-card" style="left:346px"></div>
<div class="abs nav-ring" style="left:362px"><svg viewBox="0 0 60 60" fill="none" stroke="#E4A000" stroke-width="2" stroke-linejoin="round"><path d="M10 26l20-14 20 14v22H10z"/><path d="M10 26l20 14 20-14"/><path d="M17 31V18h26v13"/></svg></div>
<div class="abs nav-btn" style="left:350px">Mail</div>

<div class="abs nav-card" style="left:521px"></div>
<div class="abs nav-ring" style="left:537px"><svg viewBox="0 0 60 60" fill="none" stroke="#E4A000" stroke-width="2" stroke-linejoin="round"><rect x="8" y="12" width="44" height="34" rx="2"/><path d="M8 19h44"/><rect x="13" y="25" width="30" height="10"/><circle cx="44" cy="42" r="5"/><path d="M48 46l5 5"/></svg></div>
<div class="abs nav-btn" style="left:525px">Web</div>

<div class="abs nav-card" style="left:696px"></div>
<div class="abs nav-ring" style="left:712px"><svg viewBox="0 0 60 60" fill="none" stroke="#E4A000" stroke-width="2"><circle cx="30" cy="26" r="15"/><ellipse cx="30" cy="26" rx="6" ry="15"/><path d="M15 26h30M18 18h24M18 34h24"/><path d="M30 41v8M22 50h16"/><path d="M12 18a20 20 0 0 0 30 26"/></svg></div>
<div class="abs nav-btn" style="left:700px">Route</div>

<div class="abs nav-card" style="left:871px"></div>
<div class="abs nav-ring" style="left:887px"><svg viewBox="0 0 60 60" fill="none" stroke="#E4A000" stroke-width="2"><rect x="12" y="8" width="36" height="12" rx="2"/><rect x="12" y="24" width="36" height="12" rx="2"/><rect x="12" y="40" width="36" height="12" rx="2"/><circle cx="18" cy="14" r="2"/><circle cx="24" cy="14" r="2"/><circle cx="18" cy="30" r="2"/><circle cx="24" cy="30" r="2"/><circle cx="18" cy="46" r="2"/><circle cx="24" cy="46" r="2"/><path d="M30 14h13M30 30h13M30 46h13"/></svg></div>
<div class="abs nav-btn" style="left:875px">Data</div>

<!-- About -->
<h2 class="abs section-title" style="top:1188px">About Us</h2>
<div class="abs about-brand"><div class="brand-name">Amber Quill</div></div>

<div class="abs about-visual" role="img" aria-label="Round photo of hands working on a white laptop"></div>

<div class="abs about-block" style="top:1410px">
  <h3>Experience</h3>
  <p>Vienna, Austria’s capital, lies in the country’s east on the Danube River. Its artistic and intellectual legacy was shaped by residents including Albrecht Venn, Jonas Keller and Emil Rauth.</p>
</div>
<div class="abs about-block" style="top:1584px">
  <h3>Highlights</h3>
  <p>The city is also known for its Imperial palaces, including Schönbrunn, the Habsburgs’ summer residence. In the MuseumsQuartier district, historic and contemporary buildings display works by Otto Brandl, Felix Morrow and other artists.</p>
</div>
<div class="abs about-block" style="top:1788px">
  <h3>Services</h3>
  <p>Until the beginning of the 20th century, Vienna was the largest German-speaking city in the world, and before the splitting of the Austro-Hungarian Empire in World War I, the city had 2 million inhabitants. Today, it is the second-largest German-speaking city after Berlin</p>
</div>

<!-- Gallery -->
<div class="abs gallery g1" role="img" aria-label="Corner building with shop entrance"></div>
<div class="abs gallery g2" role="img" aria-label="Person working on a laptop at a wooden desk"></div>
<div class="abs gallery g3" role="img" aria-label="City street with tram and historic building"></div>

<!-- Product -->
<h2 class="abs section-title" style="top:2338px">Product</h2>
<div class="abs offer" style="top:2387px">
  <div class="offer-info"><h4>Special<br>Offer</h4><p>Save up to $50 when you subscribe on annual plan</p></div>
  <div class="offer-photo photo-product" role="img" aria-label="Hands typing on a laptop on a white desk"></div>
  <div class="offer-price"><strong>$250</strong><span>Annual Plan</span></div>
</div>

<!-- Service -->
<h2 class="abs section-title" style="top:2610px">Service</h2>
<div class="abs offer" style="top:2659px">
  <div class="offer-info"><h4>Full<br>Services</h4><p>Save up to $50 when you subscribe on annual plan</p></div>
  <div class="offer-photo photo-service" role="img" aria-label="Desk from above with laptop, coffee cup and plant"></div>
  <div class="offer-price"><strong>$750</strong><span>Annual Plan</span></div>
</div>

<!-- Blog -->
<div class="abs band-blog"></div>
<h2 class="abs section-title" style="top:2944px">Our Blog</h2>

<article class="abs post" style="left:83px">
  <div class="post-photo p1" role="img" aria-label="Speaker on stage"></div>
  <div class="post-body">
    <div class="post-tag">News &amp; Update</div>
    <div class="post-title">Searchly Offers Details on Core Update Recovery Times</div>
    <div class="post-text">As we reported yesterday, Searchly has notified advertisers the search terms report will...</div>
  </div>
</article>

<article class="abs post" style="left:346px">
  <div class="post-photo p2" role="img" aria-label="Presenter in front of a blue screen"></div>
  <div class="post-body">
    <div class="post-tag">Hot Issue</div>
    <div class="post-title">Orchard Ratings is coming to OrchardOS 14, how disruptive will it be?</div>
    <div class="post-text">Orchard Maps currently relies on Reviewly and TravelNote for local business reviews and related content...</div>
  </div>
</article>

<article class="abs post" style="left:609px">
  <div class="post-photo p3" role="img" aria-label="Visitors in a gallery with framed paintings"></div>
  <div class="post-body">
    <div class="post-tag">Local News</div>
    <div class="post-title">Art lovers beware: All exhibitions you should not miss when in Vienna.</div>
    <div class="post-text">Vienna’s most famous address is finally opening its doors again at the end of August after 18 months...</div>
  </div>
</article>

<article class="abs post" style="left:873px">
  <div class="post-photo p4" role="img" aria-label="Street cafe with outdoor tables"></div>
  <div class="post-body">
    <div class="post-tag">News &amp; Update</div>
    <div class="post-title">French flair in the Servitenviertel</div>
    <div class="post-text">There’s restaurant after another in quarter in the 9th district - especially on Servitengasse...</div>
  </div>
</article>

<!-- Newsletter -->
<div class="abs newsletter"></div>
<div class="abs news-title">Subscibe our Newsletter</div>
<div class="abs news-input">Your email</div>
<div class="abs news-btn">SUBSCRIBE</div>

</body>
</html>
```